Rioja winery needs a new label design

A family-owned winery in Spain's Rioja Oriental region is looking to create a new label for a wine named "Dorvi" Arabic for Castle, that reflects the land from which the wine is born. From the remote village of Quel, La Rioja Oriental, with the backdrop of the Sierra Yerga mountains and the Barrio de Bodegas, or group of caves where locals have produced wines for centuries. Wine name:
2018 Dorvi Rioja Tempranillo
Quel, Rioja Oriental
Spain

Font styles to use
Serif
Sans Serif
Decorative
Script

Requirements
Must have
• vines, vineyards, grapes
Nice to have
• mountains,
Should not have
• castles. we already have a label design with the castle

```html
<!DOCTYPE html>
<html lang="en">
<head>
<meta charset="utf-8">
<title>Dorvi Rioja Tempranillo 2018 – Wine Label</title>
<link rel="stylesheet" href="https://fonts.googleapis.com/css2?family=Oranienbaum&family=Marcellus&family=Allura&family=Cinzel:wght@400&family=Libre+Baskerville&display=swap">
<style>
  :root {
    --backdrop: #e3e3e3;
    --frame-black: #0d0f12;
    --frame-grey: #8a8c8f;
    --paper: #f7f7f5;
    --ink-navy: #1a1f29;
    --ink-black: #07090c;
    --vintage-red: #a3161a;
    --band-text: #ffffff;
    --country-ink: #3a3c40;
    --photo-light: #cfcfcf;
    --photo-mid: #6e6e6e;
    --photo-dark: #2a2a2a;
  }
  html, body {
    margin: 0;
    padding: 0;
    width: 1200px;
    height: 820px;
    overflow: hidden;
    background: var(--backdrop);
  }
  .canvas {
    position: relative;
    width: 1200px;
    height: 820px;
    display: flex;
    align-items: center;
    justify-content: center;
  }
  .wine-label {
    width: 480px;
    height: 776px;
    display: block;
  }
  .vintage {
    font-family: "Libre Baskerville", serif;
    font-size: 50px;
    fill: var(--vintage-red);
    letter-spacing: 2px;
  }
  .wine-name {
    font-family: "Oranienbaum", serif;
    font-size: 350px;
    fill: url(#nameInk);
  }
  .varietal {
    font-family: "Marcellus", serif;
    font-size: 62px;
    fill: var(--band-text);
    letter-spacing: 1px;
  }
  .origin {
    font-family: "Allura", cursive;
    font-size: 76px;
    fill: var(--band-text);
  }
  .country {
    font-family: "Cinzel", serif;
    font-size: 46px;
    fill: var(--country-ink);
    letter-spacing: 14px;
  }
</style>
</head>
<body>
<main class="canvas">
  <svg class="wine-label" viewBox="0 0 770 1245" xmlns="http://www.w3.org/2000/svg" aria-label="Dorvi 2018 Rioja Tempranillo label">
    <defs>
      <linearGradient id="nameInk" x1="0" y1="0" x2="0" y2="1">
        <stop offset="0" stop-color="#2b3342"/>
        <stop offset="0.6" stop-color="#141922"/>
        <stop offset="1" stop-color="#050608"/>
      </linearGradient>
      <linearGradient id="bandInk" x1="0" y1="0" x2="1" y2="0">
        <stop offset="0" stop-color="#0b0d11"/>
        <stop offset="0.5" stop-color="#1f2632"/>
        <stop offset="1" stop-color="#0b0d11"/>
      </linearGradient>
      <linearGradient id="vineyardTones" x1="0" y1="0" x2="0" y2="1">
        <stop offset="0" stop-color="#3a3a3a"/>
        <stop offset="0.18" stop-color="var(--photo-light)"/>
        <stop offset="0.3" stop-color="var(--photo-mid)"/>
        <stop offset="0.6" stop-color="var(--photo-dark)"/>
        <stop offset="0.85" stop-color="#bdbdbd"/>
        <stop offset="1" stop-color="#5a5a5a"/>
      </linearGradient>
    </defs>

    <!-- label outline -->
    <path class="frame-outer" fill="var(--frame-black)"
      d="M0,160 H85 C130,60 250,0 385,0 C520,0 640,60 685,160 H770 V1080 H685 C640,1185 520,1245 385,1245 C250,1245 130,1185 85,1080 H0 Z"/>
    <path class="frame-rule" fill="var(--frame-grey)"
      d="M14,174 H94 C140,76 256,14 385,14 C514,14 630,76 676,174 H756 V1066 H676 C630,1170 514,1231 385,1231 C256,1231 140,1170 94,1066 H14 Z"/>
    <path class="frame-inner" fill="var(--frame-black)"
      d="M26,186 H102 C148,90 262,26 385,26 C508,26 622,90 668,186 H744 V1054 H668 C622,1158 508,1219 385,1219 C262,1219 148,1158 102,1054 H26 Z"/>
    <path class="paper" fill="var(--paper)"
      d="M45,200 H112 C158,104 268,40 385,40 C502,40 612,104 658,200 H725 V1040 H658 C612,1144 502,1203 385,1203 C268,1203 158,1144 112,1040 H45 Z"/>

    <text class="vintage" x="385" y="118" text-anchor="middle">- 2018 -</text>
    <text class="wine-name" x="385" y="410" text-anchor="middle" textLength="480" lengthAdjust="spacingAndGlyphs">Dorvi</text>

    <rect class="varietal-rule" x="45" y="450" width="680" height="4" fill="var(--ink-navy)"/>
    <rect class="varietal-band" x="45" y="460" width="680" height="90" fill="url(#bandInk)"/>
    <rect class="varietal-rule" x="45" y="555" width="680" height="4" fill="var(--ink-navy)"/>
    <text class="varietal" x="385" y="524" text-anchor="middle" textLength="610" lengthAdjust="spacingAndGlyphs">RIOJA TEMPRANILLO</text>

    <rect class="vineyard-photo" x="45" y="563" width="680" height="392" fill="url(#vineyardTones)"
      role="img" aria-label="Black and white photograph of vineyards in front of the Sierra Yerga mountains with a traditional earth-covered wine cave and barrels"/>

    <rect class="origin-band" x="45" y="955" width="680" height="125" fill="url(#bandInk)"/>
    <text class="origin" x="385" y="1038" text-anchor="middle">Quel | Rioja Oriental</text>

    <text class="country" x="392" y="1150" text-anchor="middle">SPAIN</text>
  </svg>
</main>
</body>
</html>
```